Flyer Information Brisk Box & Post Raleigh

I am in need of an update of my flyer that I plan on using to pass out to my customers on a daily. The prices are a must in the document, and i have provided a PDF with those prices. I have included the previous layout as the old layout is outdated and needs a fresh intake. I need the logos for all the vendors that is listed in the back of the trifold brochure as it needs to stay current.

```html
<!DOCTYPE html>
<html lang="en">
<head>
<meta charset="utf-8">
<title>Brisk Box &amp; Post Raleigh — Flyer</title>
<link href="https://fonts.googleapis.com/css2?family=Montserrat:wght@400;500;600;700;800;900&display=swap" rel="stylesheet">
<style>
:root{
  --navy:#1c2470;
  --blue:#2f3fb0;
  --sky:#3b8fe0;
  --lavender:#e8eaf7;
  --ink:#1b1f3b;
  --white:#ffffff;
  --muted:#5a6090;
  --line:#dde0f0;
  --stage:#eef0f6;
}
*{box-sizing:border-box;margin:0;padding:0}
html,body{width:867px;height:1200px;overflow:hidden;background:var(--stage)}
body{font-family:"Montserrat",Arial,sans-serif;color:var(--ink);position:relative}

.page{position:absolute;top:303px;width:420px;height:594px;background:var(--white);overflow:hidden;box-shadow:0 2px 10px rgba(28,36,112,.12)}
.page--front{left:9px}
.page--back{left:438px}

/* ---------- front ---------- */
.hero-bg{position:absolute;left:0;top:0;width:420px;height:280px;background:linear-gradient(180deg,#ffffff 0%,var(--lavender) 100%)}
.hero-photo{position:absolute;right:0;top:20px;width:205px;height:262px;background:linear-gradient(160deg,#c9d2ec 0%,#8fa6d8 55%,#3e58b8 100%)}
.brand{position:absolute;left:22px;top:20px;display:flex;align-items:center;gap:8px}
.brand-mark{width:30px;height:30px;border-radius:50%;background:var(--blue);flex:none}
.brand-name{font-weight:800;font-size:11px;line-height:1.1;color:var(--navy);text-transform:uppercase;width:110px}
.headline{position:absolute;left:22px;top:72px;width:200px;text-transform:uppercase;font-weight:800;line-height:1.05}
.headline span{display:block}
.headline .l1{font-size:19px;color:var(--navy)}
.headline .l2{font-size:19px;color:var(--sky)}
.headline .l3{font-size:20px;color:var(--navy)}
.headline .l4{font-size:14px;color:var(--navy)}
.tagline{position:absolute;left:22px;top:170px;width:180px;font-size:7.5px;line-height:1.45;color:var(--muted);font-weight:500}
.tagline strong{color:var(--navy);font-weight:700}

.welcome{position:absolute;left:0;top:232px;width:230px;height:162px;background:var(--navy);padding:13px 14px 12px 22px;color:var(--white)}
.welcome h2{font-size:9.5px;font-weight:800;text-transform:uppercase;margin-bottom:6px;line-height:1.2}
.welcome p{font-size:6.3px;line-height:1.55;color:#d8dcf5}
.welcome .dropoff{margin-top:7px;font-size:7px;font-weight:800;text-transform:uppercase;color:var(--sky);line-height:1.3}

.phone-art{position:absolute;right:14px;top:292px;width:180px;height:190px;background:radial-gradient(circle at 50% 50%,#ffd84a 0%,#ffc21a 35%,#e8ecf8 70%,#ffffff 100%);border-radius:12px}

.hours{position:absolute;left:22px;top:408px;width:200px}
.hours h3{font-size:11px;font-weight:800;color:var(--navy);text-transform:uppercase;margin-bottom:8px}
.hours ul{list-style:none}
.hours li{display:flex;align-items:center;gap:6px;font-size:7.5px;font-weight:600;margin-bottom:6px}
.hours .tick{flex:none}
.hours .day{width:58px;font-weight:800;color:var(--blue)}

.carriers{position:absolute;left:0;top:492px;width:420px;height:42px;display:flex;align-items:center;justify-content:space-around;padding:0 22px;border-top:1px solid var(--line)}
.carrier-badge{width:58px;height:19px;border-radius:3px;background:#d3d7ea}

.footer{position:absolute;left:0;bottom:0;width:420px;height:60px;background:var(--navy);display:flex;align-items:center;padding:0 18px;gap:16px;color:var(--white)}
.footer .item{display:flex;align-items:center;gap:5px;font-size:7px;font-weight:600}
.footer .label{display:block;font-size:5.5px;font-weight:500;color:#aeb5e6;text-transform:uppercase}
.footer .address{margin-left:auto;text-align:right;font-size:6.5px;line-height:1.45}

/* ---------- back ---------- */
.services-title{position:absolute;left:0;top:0;width:420px;height:44px;display:flex;align-items:center;justify-content:center}
.services-title h2{background:var(--navy);color:var(--white);font-size:11px;font-weight:800;text-transform:uppercase;letter-spacing:.5px;padding:6px 22px;border-radius:0 0 8px 8px}
.accent-bar{position:absolute;left:0;top:0;width:6px;height:534px;background:var(--blue)}
.price-columns{position:absolute;left:18px;top:52px;width:386px;display:flex;gap:12px}
.price-col{flex:1;display:flex;flex-direction:column;gap:9px}
.price-group{border:1px solid var(--line);border-radius:4px;overflow:hidden}
.price-group h3{background:var(--blue);color:var(--white);font-size:7px;font-weight:800;text-transform:uppercase;padding:4px 7px}
.price-group ul{list-style:none}
.price-group li{display:flex;justify-content:space-between;font-size:6.5px;font-weight:500;padding:3.4px 7px;border-top:1px solid var(--line)}
.price-group li:nth-child(even){background:#f5f6fc}
.price-group .price{font-weight:700;color:var(--navy)}
</style>
</head>
<body>

<section class="page page--front">
  <div class="hero-bg"></div>
  <div class="hero-photo" role="img" aria-label="Smiling delivery worker in blue uniform and cap carrying cardboard parcels in a warehouse"></div>
  <header class="brand">
    <span class="brand-mark"></span>
    <span class="brand-name">Brisk Box &amp; Post Raleigh</span>
  </header>
  <h1 class="headline">
    <span class="l1">Your Mailing</span>
    <span class="l2">and Business</span>
    <span class="l3">Service Center</span>
    <span class="l4">for over 20 years</span>
  </h1>
  <p class="tagline">Fast and friendly services for all your shipping and printing needs. <strong>Mailing, Printing, Gifts, Crafts &amp; More!</strong></p>

  <div class="welcome">
    <h2>Welcome to Brisk Box &amp; Post Raleigh</h2>
    <p>Welcome to Brisk Box &amp; Post Raleigh, your trusted neighborhood center for shipping, mailing and business services. Our friendly team has helped local families and companies for over two decades, packing with care and sending worldwide. Stop by today and let us handle the details.</p>
    <p class="dropoff">Convenient drop off location<br>for your packages</p>
  </div>

  <div class="phone-art" role="img" aria-label="Illustration of a smartphone with a check mark on screen surrounded by parcels on a yellow burst"></div>

  <div class="hours">
    <h3>Operating Hours</h3>
    <ul>
      <li><svg class="tick" width="11" height="11" viewBox="0 0 20 20"><circle cx="10" cy="10" r="10" fill="#2f3fb0"/><path d="M5.5 10.5l3 3 6-6.5" stroke="#fff" stroke-width="2.4" fill="none" stroke-linecap="round" stroke-linejoin="round"/></svg><span class="day">Mon – Fri</span><span>9:00am to 6:30pm</span></li>
      <li><svg class="tick" width="11" height="11" viewBox="0 0 20 20"><circle cx="10" cy="10" r="10" fill="#2f3fb0"/><path d="M5.5 10.5l3 3 6-6.5" stroke="#fff" stroke-width="2.4" fill="none" stroke-linecap="round" stroke-linejoin="round"/></svg><span class="day">Saturday</span><span>10:00am to 3:00pm</span></li>
      <li><svg class="tick" width="11" height="11" viewBox="0 0 20 20"><circle cx="10" cy="10" r="10" fill="#2f3fb0"/><path d="M5.5 10.5l3 3 6-6.5" stroke="#fff" stroke-width="2.4" fill="none" stroke-linecap="round" stroke-linejoin="round"/></svg><span class="day">Sunday</span><span>Closed</span></li>
    </ul>
  </div>

  <div class="carriers">
    <span class="carrier-badge"></span>
    <span class="carrier-badge"></span>
    <span class="carrier-badge"></span>
    <span class="carrier-badge"></span>
  </div>

  <footer class="footer">
    <div class="item">
      <svg width="13" height="13" viewBox="0 0 24 24"><path d="M6.6 10.8a15.2 15.2 0 006.6 6.6l2.2-2.2c.3-.3.7-.4 1-.2 1.1.4 2.3.6 3.6.6.6 0 1 .4 1 1V20c0 .6-.4 1-1 1A17 17 0 013 4c0-.6.4-1 1-1h3.5c.6 0 1 .4 1 1 0 1.3.2 2.5.6 3.6.1.3 0 .7-.2 1z" fill="#3b8fe0"/></svg>
      <span><span class="label">Call us now</span>(919) 555-0142</span>
    </div>
    <div class="item">
      <svg width="13" height="13" viewBox="0 0 24 24"><circle cx="12" cy="12" r="9" fill="none" stroke="#3b8fe0" stroke-width="2"/><path d="M3 12h18M12 3c3 3 3 15 0 18M12 3c-3 3-3 15 0 18" fill="none" stroke="#3b8fe0" stroke-width="1.6"/></svg>
      <span><span class="label">Website</span>www.briskboxpost.com</span>
    </div>
    <div class="address">Brisk Box &amp; Post Raleigh<br>4820 Oakmont Rd, Suite 110<br>Raleigh, NC 27612</div>
  </footer>
</section>

<section class="page page--back">
  <div class="accent-bar"></div>
  <div class="services-title"><h2>Services that we offer</h2></div>

  <div class="price-columns">
    <div class="price-col">
      <div class="price-group">
        <h3>Shipping Services</h3>
        <ul>
          <li><span>Ground Shipping</span><span class="price">$9.99</span></li>
          <li><span>Express Overnight</span><span class="price">$29.99</span></li>
          <li><span>International</span><span class="price">$39.99</span></li>
          <li><span>Freight Quote</span><span class="price">Free</span></li>
          <li><span>Package Pickup</span><span class="price">$5.00</span></li>
        </ul>
      </div>
      <div class="price-group">
        <h3>Mailbox Services</h3>
        <ul>
          <li><span>Small Box (3 mo)</span><span class="price">$45.00</span></li>
          <li><span>Medium Box (3 mo)</span><span class="price">$60.00</span></li>
          <li><span>Large Box (3 mo)</span><span class="price">$85.00</span></li>
          <li><span>Mail Forwarding</span><span class="price">$10.00</span></li>
        </ul>
      </div>
      <div class="price-group">
        <h3>Business Services</h3>
        <ul>
          <li><span>Notary Public</span><span class="price">$10.00</span></li>
          <li><span>Fingerprinting</span><span class="price">$20.00</span></li>
          <li><span>Passport Photos</span><span class="price">$15.00</span></li>
          <li><span>Shredding per lb</span><span class="price">$1.00</span></li>
          <li><span>Key Copies</span><span class="price">$3.50</span></li>
        </ul>
      </div>
      <div class="price-group">
        <h3>Packing Supplies</h3>
        <ul>
          <li><span>Small Box</span><span class="price">$2.50</span></li>
          <li><span>Medium Box</span><span class="price">$4.00</span></li>
          <li><span>Large Box</span><span class="price">$6.00</span></li>
          <li><span>Bubble Wrap per ft</span><span class="price">$0.50</span></li>
          <li><span>Packing Tape</span><span class="price">$4.99</span></li>
        </ul>
      </div>
    </div>

    <div class="price-col">
      <div class="price-group">
        <h3>Printing &amp; Copies</h3>
        <ul>
          <li><span>Black &amp; White Copy</span><span class="price">$0.15</span></li>
          <li><span>Color Copy</span><span class="price">$0.79</span></li>
          <li><span>Business Cards (250)</span><span class="price">$29.00</span></li>
          <li><span>Flyers (100)</span><span class="price">$35.00</span></li>
          <li><span>Posters</span><span class="price">$18.00</span></li>
          <li><span>Banners</span><span class="price">$45.00</span></li>
        </ul>
      </div>
      <div class="price-group">
        <h3>Fax &amp; Scan</h3>
        <ul>
          <li><span>Fax Local</span><span class="price">$1.50</span></li>
          <li><span>Fax Long Distance</span><span class="price">$2.50</span></li>
          <li><span>Fax International</span><span class="price">$5.00</span></li>
          <li><span>Scan to Email</span><span class="price">$1.00</span></li>
        </ul>
      </div>
      <div class="price-group">
        <h3>Packing Services</h3>
        <ul>
          <li><span>Custom Crating</span><span class="price">Quote</span></li>
          <li><span>Gift Wrapping</span><span class="price">$5.00</span></li>
          <li><span>Fragile Packing</span><span class="price">$12.00</span></li>
          <li><span>Electronics Packing</span><span class="price">$15.00</span></li>
        </ul>
      </div>
      <div class="price-group">
        <h3>Office Extras</h3>
        <ul>
          <li><span>Laminating</span><span class="price">$3.00</span></li>
          <li><span>Binding</span><span class="price">$6.00</span></li>
          <li><span>Computer Rental / min</span><span class="price">$0.30</span></li>
          <li><span>Postage Stamps</span><span class="price">Cost</span></li>
          <li><span>Greeting Cards</span><span class="price">$3.99</span></li>
        </ul>
      </div>
    </div>
  </div>

  <footer class="footer">
    <div class="item">
      <svg width="13" height="13" viewBox="0 0 24 24"><path d="M6.6 10.8a15.2 15.2 0 006.6 6.6l2.2-2.2c.3-.3.7-.4 1-.2 1.1.4 2.3.6 3.6.6.6 0 1 .4 1 1V20c0 .6-.4 1-1 1A17 17 0 013 4c0-.6.4-1 1-1h3.5c.6 0 1 .4 1 1 0 1.3.2 2.5.6 3.6.1.3 0 .7-.2 1z" fill="#3b8fe0"/></svg>
      <span><span class="label">Call us now</span>(919) 555-0142</span>
    </div>
    <div class="item">
      <svg width="13" height="13" viewBox="0 0 24 24"><circle cx="12" cy="12" r="9" fill="none" stroke="#3b8fe0" stroke-width="2"/><path d="M3 12h18M12 3c3 3 3 15 0 18M12 3c-3 3-3 15 0 18" fill="none" stroke="#3b8fe0" stroke-width="1.6"/></svg>
      <span><span class="label">Website</span>www.briskboxpost.com</span>
    </div>
    <div class="address">Brisk Box &amp; Post Raleigh<br>4820 Oakmont Rd, Suite 110<br>Raleigh, NC 27612</div>
  </footer>
</section>

</body>
</html>
```